Flyer Advertisement Simple But Creative

Flyer dimensions 4" x 6"

Simple design with logo and additional info. On the front of the flyer:

- place the logo at the top
- beneath the logo add the website and phone number
- simple less is more approach
- feel free to add your own personal touch

On the back:

- Requirements
- Perfect for Birthdays and Anniversaries
- Rentals available hourly, daily, and weekly
- Group Rentals available at discounted rates
- Enter to win a free rental - url and QR code

Industry/Entity Type

Car Rental

Font styles to use
Serif
Sans Serif

Colors

Designer to choose colors to be used in the design.

Requirements
Must have
• FRONT:
• Please include our phone number and website:
• 614-287-3951
• www.BrindlewoodTrikeHire.example
• BACK:
• REQUIREMENTS
• At least 25 years of age
• Valid Driver's License
• Debit or Credit Card
• Must know how to drive a manual transmission or stick shift

```html
<!DOCTYPE html>
<html lang="en">
<head>
<meta charset="utf-8">
<title>Brindlewood Trike Hire – Flyer Front and Back</title>
<link rel="stylesheet" href="https://fonts.googleapis.com/css2?family=Roboto:wght@400;700;900&display=swap">
<style>
  :root {
    --stage: #2b2b2b;
    --paper: #ffffff;
    --paper-grey: #efeff1;
    --ink: #081418;
    --red: #ec1848;
    --red-deep: #e4062e;
    --text-dark: #1a1a1a;
    --text-light: #ffffff;
  }
  * { box-sizing: border-box; margin: 0; padding: 0; }
  html, body { width: 1200px; height: 800px; overflow: hidden; }
  body {
    background: var(--stage);
    font-family: "Roboto", Arial, sans-serif;
    position: relative;
  }
  .flyer {
    position: absolute;
    top: 55px;
    width: 460px;
    height: 690px;
    background: var(--paper);
    overflow: hidden;
    box-shadow: 0 12px 30px rgba(0,0,0,.45);
  }
  .flyer--front { left: 110px; }
  .flyer--back { left: 630px; }
  .flyer__shapes { position: absolute; inset: 0; width: 100%; height: 100%; }

  .brand {
    position: absolute;
    display: flex;
    align-items: center;
    gap: 8px;
  }
  .brand__mark { width: 14px; height: 14px; background: var(--red); flex: none; }
  .brand__name {
    font-weight: 900;
    font-size: 17px;
    line-height: 1.1;
    color: var(--text-dark);
    text-transform: uppercase;
    letter-spacing: .5px;
  }
  .flyer--front .brand { left: 24px; top: 70px; width: 170px; }
  .flyer--back .brand { left: 300px; top: 450px; width: 150px; }

  .contact {
    position: absolute;
    right: 16px;
    top: 585px;
    color: var(--text-light);
    text-align: right;
    white-space: nowrap;
  }
  .contact__phone { font-size: 22px; font-weight: 400; letter-spacing: .5px; }
  .contact__web { font-size: 12.5px; font-weight: 400; margin-top: 10px; }

  .requirements {
    position: absolute;
    left: 34px;
    top: 500px;
    width: 220px;
    color: var(--text-dark);
  }
  .requirements__title {
    color: var(--red);
    font-weight: 700;
    font-size: 22px;
    letter-spacing: .3px;
    margin-bottom: 6px;
  }
  .requirements__list { list-style: none; }
  .requirements__item {
    position: relative;
    padding-left: 18px;
    font-size: 15px;
    line-height: 1.35;
    margin-bottom: 2px;
  }
  .requirements__item::before {
    content: "";
    position: absolute;
    left: 4px;
    top: 9px;
    width: 3px;
    height: 3px;
    background: var(--red);
  }
</style>
</head>
<body>

  <section class="flyer flyer--front" aria-label="Flyer front">
    <svg class="flyer__shapes" viewBox="0 0 460 690">
      <defs>
        <linearGradient id="photo-garage" x1="0" y1="0" x2="1" y2="1">
          <stop offset="0" stop-color="#3c3f44"/><stop offset="1" stop-color="#1e3a55"/>
        </linearGradient>
        <linearGradient id="photo-blue" x1="0" y1="0" x2="1" y2="1">
          <stop offset="0" stop-color="#56585c"/><stop offset=".5" stop-color="#1d2c6a"/><stop offset="1" stop-color="#4a4845"/>
        </linearGradient>
        <linearGradient id="photo-grey" x1="0" y1="0" x2="0" y2="1">
          <stop offset="0" stop-color="#c9d0d8"/><stop offset=".6" stop-color="#6d7177"/><stop offset="1" stop-color="#b7b3ad"/>
        </linearGradient>
        <linearGradient id="photo-main" x1="0" y1="0" x2="0" y2="1">
          <stop offset="0" stop-color="#e2e6ea"/><stop offset=".5" stop-color="#9da2a8"/><stop offset="1" stop-color="#8c857b"/>
        </linearGradient>
      </defs>
      <rect x="0" y="0" width="460" height="690" fill="var(--paper-grey)"/>
      <rect x="195" y="0" width="120" height="165" fill="var(--ink)"/>
      <polygon points="290,0 460,0 460,230 370,230" fill="var(--red)"/>
      <polygon points="250,300 460,300 460,560 340,560" fill="var(--red)"/>
      <rect x="0" y="180" width="140" height="150" fill="url(#photo-garage)" role="img" aria-label="Photo of a three-wheel roadster in a parking garage"/>
      <rect x="145" y="168" width="150" height="160" fill="url(#photo-blue)" role="img" aria-label="Photo of a blue three-wheel roadster"/>
      <rect x="300" y="158" width="160" height="132" fill="url(#photo-grey)" role="img" aria-label="Photo of a grey three-wheel roadster by a cloudy sky"/>
      <rect x="0" y="335" width="340" height="260" fill="url(#photo-main)" role="img" aria-label="Photo of a silver three-wheel roadster in a parking lot"/>
      <rect x="200" y="560" width="260" height="130" fill="var(--ink)"/>
    </svg>
    <div class="brand">
      <span class="brand__mark"></span>
      <span class="brand__name">Brindlewood Trike Hire</span>
    </div>
    <div class="contact">
      <p class="contact__phone">T : 614-287-3951</p>
      <p class="contact__web">W : www.BrindlewoodTrikeHire.example</p>
    </div>
  </section>

  <section class="flyer flyer--back" aria-label="Flyer back">
    <svg class="flyer__shapes" viewBox="0 0 460 690">
      <defs>
        <linearGradient id="photo-cockpit" x1="0" y1="0" x2="1" y2="1">
          <stop offset="0" stop-color="#e8e8e8"/><stop offset=".4" stop-color="#3a3a3c"/><stop offset="1" stop-color="#0d0d0f"/>
        </linearGradient>
      </defs>
      <rect x="0" y="0" width="460" height="690" fill="var(--paper-grey)"/>
      <polygon points="40,0 460,0 460,360 330,420 90,150" fill="url(#photo-cockpit)" role="img" aria-label="Photo of a roadster cockpit with steering wheel and gauges"/>
      <polygon points="0,40 0,110 250,420 330,400 90,130 20,20" fill="var(--red-deep)" opacity=".92"/>
      <polygon points="0,110 0,180 210,425 250,420" fill="var(--paper)"/>
    </svg>
    <div class="brand">
      <span class="brand__mark"></span>
      <span class="brand__name">Brindlewood Trike Hire</span>
    </div>
    <div class="requirements">
      <h2 class="requirements__title">REQUIREMENTS</h2>
      <ul class="requirements__list">
        <li class="requirements__item">At least 25 years of age</li>
        <li class="requirements__item">Valid Driver's License</li>
        <li class="requirements__item">Debit or Credit Card</li>
        <li class="requirements__item">Must know how to drive a manual transmission or stick shift</li>
      </ul>
    </div>
  </section>

</body>
</html>
```